Halvorine Ledgers & Advisory Tri-Fold Brochure (8.5"x11")

I need a professional looking brochure for my bookkeeping business. I am looking for something professional yet casual (not too corporate looking). I have attached a sample brochure that will outline the areas and a copy of our logo. I'd like to stick with shades of blue. The final product should communicate professional and personal.

Target Market(s)

Small service businesses.

Industry/Entity Type

Business

Font styles to use
Sans Serif

Requirements
Must have
• Professional looking photos of people in areas where it asks for a picture.

```html
<!DOCTYPE html>
<html lang="en">
<head>
<meta charset="utf-8">
<title>Halvorine Ledgers &amp; Advisory – Tri-Fold Brochure</title>
<link href="https://fonts.googleapis.com/css2?family=Ubuntu:wght@300;400;500;700&display=swap" rel="stylesheet">
<style>
  :root {
    --sky: #4ec5f1;
    --sky-deep: #2fb3e6;
    --ink: #2a2a2b;
    --paper: #ffffff;
    --paper-soft: #f4f6f7;
    --text-dark: #3a3d40;
    --stage: #a9b1b2;
  }
  * { box-sizing: border-box; margin: 0; padding: 0; }
  html, body {
    width: 1200px; height: 900px; overflow: hidden;
    background: var(--stage);
    font-family: "Ubuntu", Arial, sans-serif;
  }
  .brochure {
    position: absolute; left: 75px; top: 50px;
    width: 1050px; height: 800px;
    display: flex;
    background: var(--paper);
    box-shadow: 0 10px 30px rgba(0,0,0,.18);
  }
  .panel {
    width: 350px; height: 100%;
    display: flex; flex-direction: column;
    padding: 22px 20px 0;
    border-right: 1px solid #e4e8ea;
  }
  .panel:last-child { border-right: none; }
  .panel--middle { background: var(--paper-soft); }

  .block {
    background: var(--sky);
    color: var(--paper);
    font-weight: 300;
    font-size: 13.5px;
    line-height: 1.38;
    padding: 12px 16px;
  }
  .section-title {
    color: var(--text-dark);
    font-weight: 500;
    font-size: 14.5px;
    text-align: center;
    padding: 8px 0 7px;
  }

  /* left panel */
  .hero {
    background: var(--sky);
    display: flex; flex-direction: column; align-items: center;
    padding: 22px 0 14px;
  }
  .hero-icon { width: 120px; height: 120px; }
  .hero-title {
    color: var(--paper); font-weight: 400; font-size: 46px;
    letter-spacing: 1px; margin-top: 10px;
  }
  .footer-bar {
    margin: auto -20px 0;
    background: var(--ink); color: var(--paper);
    font-size: 22px; letter-spacing: 1px;
    text-align: center; padding: 13px 0 14px;
  }

  /* middle panel */
  .why { padding: 8px 16px 12px; }
  .why-title { text-align: center; font-weight: 500; font-size: 14px; margin-bottom: 6px; }
  .why-list {
    list-style: none; display: grid; grid-template-columns: 1fr 1fr;
    font-size: 13px; row-gap: 2px;
  }
  .why-list li::before, .bullet-list li::before {
    content: "◉"; font-size: 9px; margin-right: 6px; vertical-align: 1px; opacity: .8;
  }
  .headline {
    background: var(--ink); color: var(--paper);
    text-align: center; text-transform: uppercase;
    padding: 16px 10px 18px; margin: 14px 0 12px;
    font-weight: 300; line-height: 1.12;
  }
  .headline-small { font-size: 21px; letter-spacing: .5px; }
  .headline-large { font-size: 33px; font-weight: 500; }
  .process-title {
    background: var(--sky); color: var(--paper);
    text-align: center; font-weight: 500; font-size: 14px; padding: 7px 0;
  }
  .process-steps {
    list-style: none; text-align: center;
    color: var(--text-dark); font-size: 13.5px; line-height: 1.35;
    padding: 18px 10px 0;
  }
  .process-steps li { margin-bottom: 17px; }
  .brand {
    margin-top: auto; margin-bottom: 60px;
    display: flex; align-items: center; justify-content: center; gap: 10px;
  }
  .brand-mark { width: 22px; height: 22px; background: var(--sky); border-radius: 50%; flex: none; }
  .brand-name { color: var(--sky-deep); font-weight: 500; font-size: 22px; line-height: 1.15; }

  /* right panel */
  .continued-title {
    background: var(--sky); color: var(--paper);
    text-align: center; text-transform: uppercase;
    font-size: 30px; line-height: 1.05; padding: 12px 0 10px;
  }
  .bullet-list { list-style: none; }
</style>
</head>
<body>
  <main class="brochure">

    <section class="panel panel--left">
      <div class="hero">
        <svg class="hero-icon" viewBox="0 0 120 120" role="img" aria-label="Lightbulb icon">
          <circle cx="60" cy="60" r="58" fill="var(--paper)"/>
          <circle cx="60" cy="60" r="52" fill="none" stroke="var(--sky)" stroke-width="1.5" stroke-dasharray="4 3"/>
          <circle cx="60" cy="58" r="22" fill="var(--sky)" opacity=".35"/>
        </svg>
        <h1 class="hero-title">SERVICES</h1>
      </div>
      <h2 class="section-title">Full Charge Bookkeeping</h2>
      <p class="block">We can manage all aspects of your bookkeeping and business financials and communicate to you as much and as often as you want.</p>
      <h2 class="section-title">Cash Management (Bill Pay &amp; Invoicing) &amp; Vendor Management</h2>
      <p class="block">We can handle every step from receiving bills, communicating with vendor and paying bills. We take a lot pride in helping our clients save money and one way is negotiating with vendors and finding appropriate discounts.</p>
      <h2 class="section-title">Financial Statements</h2>
      <p class="block">Profit and Loss – Balance Sheet – Statement of Cash Flow – Industry Specific. We accurately prepare monthly, quarterly &amp; annual financial statements in a timely manner. We also take the time to review these statements with you so that you understand the financial health of your business.</p>
      <div class="footer-bar">555.014.2290</div>
    </section>

    <section class="panel panel--middle">
      <div class="block why">
        <h2 class="why-title">Why Outsource Bookkeeping?</h2>
        <ul class="why-list">
          <li>Save Time</li><li>Focused Staff</li>
          <li>Save Money</li><li>Technology</li>
          <li>Expertise</li><li>Experience</li>
        </ul>
      </div>
      <div class="headline">
        <div class="headline-small">The Financial Numbers</div>
        <div class="headline-large">Are the Heart</div>
        <div class="headline-small">Beat of an Organization</div>
      </div>
      <h2 class="process-title">The Process</h2>
      <ol class="process-steps">
        <li>Contact Us – we like to hear from you</li>
        <li>No-Obligation Consultation<br>Review Current Process – identify strengths and weaknesses</li>
        <li>Recommend and implement new bookkeeping process</li>
        <li>Ongoing bookkeeping partnership</li>
        <li>Provide your company with more value and service to keep earning your business (ongoing)</li>
      </ol>
      <div class="brand">
        <span class="brand-mark"></span>
        <span class="brand-name">Halvorine Ledgers<br>&amp; Advisory</span>
      </div>
    </section>

    <section class="panel panel--right">
      <h1 class="continued-title">Services<br>(Continued)</h1>
      <h2 class="section-title">Account Reconciliations</h2>
      <p class="block">From bank account to credit card statements to vendor statements. We reconcile all of your accounts that impact your finances.</p>
      <h2 class="section-title">Professional liaison</h2>
      <p class="block">We will work directly with your other business partners – Bankers, CPA, Insurance, Payroll, Attorney… Need a loan? We will work directly with your banker to make the process as simple as possible. Does your CPA need some data? Let us take care of that while you continue making your customers happy.</p>
      <h2 class="section-title">Business Services</h2>
      <ul class="block bullet-list">
        <li>Budget</li>
        <li>Create Proper Financial Systems</li>
        <li>Projections</li>
        <li>Customized Reporting</li>
        <li>Protection Planning</li>
        <li>Benchmarking</li>
        <li>Online Filing Cabinet (Paperless)</li>
      </ul>
      <h2 class="section-title">Exit/Succession Planning</h2>
      <p class="block">We help you prepare your business for the next transition – planned (retirement) or unplanned (health). You've sacrificed to build this business (asset) we can help you transition it in the most efficient and valuable way.</p>
      <div class="footer-bar" style="font-size:19px">mara@halvorineledgers.com</div>
    </section>

  </main>
</body>
</html>
```